Flyer Design for a Boston Therapeutic Clinic

I am a body therapist who needs a couple of flyers designed:
1. To fit half a page.
2. To fit a 5 inch by 3.5 inch flyer.
My practice is based in Boston, MA and my web site is:
www.LarkfieldTane.Com
For the First half page:
A. Have my company's name and color shown as it appears on my web site (Larkfield Tane)
B. Have the following text: "Control your weight (This part should be emphasized) by balancing your nervous and digestive system through the Tane Method. The Tane Method, a technique developed by Dr. Wenna. Tane, uses physical pressure to manipulate visceral tissue to bring back resiliency and proper functioning of the whole body."
Also helps with
-Constipation
-Bloating
-IBS
-eating disorders and overeating
Our practitioner is highly experienced. Please visit our web sites for reviews.
C. I would like to have a nice earthy feeling, something that feels "freeing" like open flowers, or an open land scape such as mountains or fields.
D. I also like the color blue, white, orange; perhaps if these colors can be integrated into the flyer, that would be great.
E. "Visit our web site LarkfieldTane.com or call 413-908-2617"
The Smaller Flyer :
A.The smaller Flyer should also have my Company's name as shown on my web site (Larkfield Tane)
B.The following text: " Restore your body's natural resiliency and greatly reduce your physical pain through the Dr. Wenna Tane Method of Structural Integration."
C. "Our practitioner is highly experienced and has a great reputation; visit our web site for reviews."
"Benefits:
"reduce aches and pains
reduce joint pain
reduce chronic muscular tension"
D, "feel better after the first session!"
E. if you could use a picture of me working on someone from my web site, that would be great.
F. I also like the colors white, orange and silver, for this one.
G. "Visit our web site LarkfieldTane.com or call 413-908 2617"
I am very open minded,
I would like the flyer to evoke a sense of tranquility, professionalism, and simplicity. So if you have another angle you think would look good, then go for it! As long as it looks clean, professional and helpful.
Thanks a lot!
If you need any pictures from my web site, I have the original high resolution files that i can send.
Professionals and working men and women from ages 20-70
Clinic

```html
<!DOCTYPE html>
<html lang="en">
<head>
<meta charset="utf-8">
<title>Larkfield Tane Therapy — Flyers</title>
<link rel="stylesheet" href="https://fonts.googleapis.com/css2?family=Roboto:wght@400;700&family=Roboto+Condensed:wght@400;700&family=Josefin+Slab:wght@400&family=Kanit:wght@500&display=swap">
<style>
  :root {
    --stage: #707070;
    --orange: #f0602a;
    --orange-warm: #f58a1f;
    --gold: #fcc21a;
    --ink: #1e1e1e;
    --grey-ink: #5a5a5a;
    --navy: #25307a;
    --sky: #2ba3dc;
    --yellow-text: #f6ea3a;
    --silver-light: #f4f4f4;
    --silver-mid: #b9b9b9;
    --bullet: #d23a2a;
  }
  * { margin: 0; padding: 0; box-sizing: border-box; }
  html, body { width: 1200px; height: 543px; overflow: hidden; }
  body { background: var(--stage); position: relative; font-family: "Roboto", Arial, sans-serif; }

  .flyer { position: absolute; overflow: hidden; }

  /* Half-page flyer */
  .half-page { left: 30px; top: 26px; width: 692px; height: 490px;
    background: linear-gradient(180deg, #f1f1f1 0%, #ffffff 40%, #f0f0f0 100%); }
  .half-page .landscape { position: absolute; left: 0; top: 0; width: 692px; height: 192px;
    background: linear-gradient(180deg, #cfe0ee 0%, #9fb4c6 30%, #7b8aa0 50%, #b5734a 75%, #d9782f 100%); }
  .half-page .landscape-rule { position: absolute; left: 0; top: 192px; width: 692px; height: 5px;
    background: linear-gradient(90deg, var(--orange), var(--orange-warm)); }
  .brand-name { position: absolute; font-family: "Josefin Slab", Georgia, serif; font-weight: 400;
    color: var(--grey-ink); white-space: nowrap; }
  .half-page .brand-name { right: 34px; top: 234px; font-size: 34px; }

  .headline { position: absolute; left: 34px; top: 270px; font-family: "Roboto Condensed", Arial, sans-serif;
    font-weight: 700; font-size: 23px; color: var(--orange); }
  .intro { position: absolute; left: 34px; top: 300px; width: 372px; font-size: 13.2px; line-height: 17px;
    color: var(--ink); text-align: justify; }
  .also-helps { position: absolute; left: 445px; top: 296px; font-size: 13.5px; color: var(--ink); }
  .also-helps ul { list-style: none; margin-top: 10px; }
  .also-helps li { position: relative; padding-left: 13px; line-height: 21px; font-size: 13.5px; }
  .also-helps li::before { content: ""; position: absolute; left: 0; top: 7px; width: 7px; height: 7px;
    border-radius: 50%; background: radial-gradient(circle at 35% 35%, #f29a8a, var(--bullet)); }

  .contact-band { position: absolute; left: 0; top: 406px; width: 692px; height: 84px; }
  .contact-band .rule-top { height: 4px; background: var(--orange-warm); }
  .contact-band .band { height: 54px; background: linear-gradient(180deg, var(--sky) 0%, #2a5ea8 50%, var(--navy) 100%);
    text-align: center; padding-top: 5px; }
  .contact-band .rule-bottom { height: 26px; background: linear-gradient(90deg, var(--orange) 0%, var(--gold) 50%, var(--orange) 100%); margin-top: 0; }
  .reviews-note { color: var(--yellow-text); font-size: 14.5px; }
  .call-to-action { font-family: "Kanit", Arial, sans-serif; font-weight: 500; color: var(--orange-warm);
    font-size: 21px; line-height: 28px; margin-top: 1px; letter-spacing: 0.2px; }

  /* Small flyer */
  .small-card { left: 746px; top: 51px; width: 418px; height: 293px; background: #ffffff; }
  .small-card .portrait { position: absolute; left: 0; top: 0; width: 196px; height: 144px;
    background: linear-gradient(90deg, #a93b12 0%, #e0611f 55%, #f07a2a 100%); }
  .small-card .header-silver { position: absolute; left: 196px; top: 0; width: 222px; height: 144px;
    background: linear-gradient(180deg, #a5a5a5 0%, #dcdcdc 50%, #fbfbfb 100%); }
  .small-card .brand-name { right: 15px; top: 118px; font-size: 17.5px; }
  .small-card .header-rule { position: absolute; left: 0; top: 144px; width: 418px; height: 2px; background: var(--orange); }
  .small-body { position: absolute; left: 18px; top: 154px; width: 196px; font-size: 8.7px; line-height: 11px;
    color: var(--ink); text-align: justify; }
  .small-body p + p { margin-top: 11px; }
  .benefits { position: absolute; left: 231px; top: 155px; }
  .benefits h3 { font-family: "Roboto Condensed", Arial, sans-serif; font-weight: 700; font-size: 11px; color: var(--orange); }
  .benefits ul { list-style: none; margin-top: 7px; }
  .benefits li { display: flex; align-items: center; gap: 5px; font-size: 9.6px; color: var(--ink); height: 17.5px; }
  .benefits svg { width: 9px; height: 9px; flex: none; }
  .tagline { font-family: "Roboto Condensed", Arial, sans-serif; font-weight: 700; font-size: 12.5px; color: var(--orange); margin-top: 6px; }
  .small-contact { position: absolute; left: 0; top: 253px; width: 418px; height: 25px;
    border-top: 1px solid #8c8c8c;
    background: linear-gradient(180deg, #9a9a9a 0%, var(--silver-light) 45%, #c9c9c9 100%);
    text-align: center; font-family: "Kanit", Arial, sans-serif; font-weight: 500; font-size: 12.2px; line-height: 24px;
    color: var(--orange); letter-spacing: 0.3px; }
  .small-card .footer-bar { position: absolute; left: 0; top: 281px; width: 418px; height: 12px;
    background: linear-gradient(90deg, var(--orange) 0%, var(--orange-warm) 50%, var(--orange) 100%); }
</style>
</head>
<body>

<section class="flyer half-page">
  <div class="landscape" role="img" aria-label="Open mountain valley with autumn-coloured slopes under a pale sky"></div>
  <div class="landscape-rule"></div>
  <div class="brand-name">Larkfield Tane Therapy</div>

  <h2 class="headline">Control your weight</h2>
  <p class="intro">by balancing your nervous and digestive system through the Tane Method. The Tane Method, a technique developed by Dr. Wenna. Tane, uses physical pressure to manipulate visceral tissue to bring back resiliency and proper functioning of the whole body.</p>

  <div class="also-helps">
    <p>Also helps with</p>
    <ul>
      <li>Constipation</li>
      <li>Bloating</li>
      <li>IBS</li>
      <li>eating disorders and overeating</li>
    </ul>
  </div>

  <div class="contact-band">
    <div class="rule-top"></div>
    <div class="band">
      <p class="reviews-note">Our practitioner is highly experienced. Please visit our web sites for reviews.</p>
      <p class="call-to-action">Visit our web site LarkfieldTane.com or call 413-908-2617</p>
    </div>
    <div class="rule-bottom"></div>
  </div>
</section>

<section class="flyer small-card">
  <div class="portrait" role="img" aria-label="Photo of a man seated, holding his knee, against a warm orange backdrop"></div>
  <div class="header-silver"></div>
  <div class="brand-name">Larkfield Tane Therapy</div>
  <div class="header-rule"></div>

  <div class="small-body">
    <p>Restore your body's natural resiliency and greatly reduce your physical pain through the Dr. Wenna Tane Method of Structural Integration.</p>
    <p>Our practitioner is highly experienced and has a great reputation; visit our web site for reviews.physical pain through the Dr. Wenna Tane Method of Structural Integration.</p>
  </div>

  <div class="benefits">
    <h3>Benefits:</h3>
    <ul>
      <li><svg viewBox="0 0 10 10"><rect x="0.5" y="1.5" width="7.5" height="7.5" fill="none" stroke="#f0602a" stroke-width="1"/><path d="M2 5 L4 7.2 L9.5 0.8" fill="none" stroke="#f0602a" stroke-width="1.5"/></svg>reduce aches and pains</li>
      <li><svg viewBox="0 0 10 10"><rect x="0.5" y="1.5" width="7.5" height="7.5" fill="none" stroke="#f0602a" stroke-width="1"/><path d="M2 5 L4 7.2 L9.5 0.8" fill="none" stroke="#f0602a" stroke-width="1.5"/></svg>reduce joint pain</li>
      <li><svg viewBox="0 0 10 10"><rect x="0.5" y="1.5" width="7.5" height="7.5" fill="none" stroke="#f0602a" stroke-width="1"/><path d="M2 5 L4 7.2 L9.5 0.8" fill="none" stroke="#f0602a" stroke-width="1.5"/></svg>reduce chronic muscular tension</li>
    </ul>
    <p class="tagline">feel better after the first session!</p>
  </div>

  <div class="small-contact">Visit our web site LarkfieldTane.com or call 413-908 2617</div>
  <div class="footer-bar"></div>
</section>

</body>
</html>
```